Infografik/ Zeitleiste für Startup
Zielgruppe
Wir sind ein Startup, das über die Seite Zeitwabe.de zukünftig folgenden Service anbietet: Unternehmer können sehr flexibel (selbst) gestaltete Terminformulare erstellen und auf Ihrer Website einbinden. Kunden können dann diese Termine buchen und bekommen dann Erinnerungs-Mails und SMS.
Zielgruppe: Dienstleister wie Fotografen, Friseure, Versicherungsvertreter, Masseure, Restaurants, Arztpraxen. Also alle, die darauf angewiesen sind, dass vereinbarte Termine eingehalten werden und die die Terminvereinbarung vereinfachen wollen. Also weniger per Telefon, mehr über die eigene Website.
Zeitwabe ist mit LobPunkt.com (aktuell noch Top-und-Flop.com) verknüpft. Kunden, die einen Termin wünschen, sehen die Bewertungen vorheriger Kunden. Das stärkt das Vertrauen und erhöht die Termin-Zuverlässigkeit (Verbessert die No-Show-Rate). Damit sinken auch die Werbekosten je Kunden (geringere Kosten pro Conversion).
Zeitwabe.de und LobPunkt.com (aktuell noch Top-und-Flop.com) wurde vom Team von Bild-Kontor.de entwickelt. Dank Zeitwabe und LobPunkt.com haben wir (das Team von Bild-Kontor.de) folgende Vorteile:
- verbesserte Termin-Zuverlässigkeit (No-Show-Rate)
- mehr Kunden, mehr Shootings
- höherer Umsatz
- Zeitersparnis bei der Terminvereinbarung
- Senkungen der Werbekosten je Kunden (geringere Kosten pro Conversion)
Das ist der Grund, warum wir Zeitwabe und LobPunkt nun auch für andere Branchen anbieten.
Siehe auch: https://www.videoportal-beispiel.de/watch?v=qRtmZZk_31p
Siehe auch: https://www.videoportal-beispiel.de/watch?v=wLpoNNe_74x
Aufgabenstellung
Wir benötigen für Zeitwabe.de eine Infografik. Diese soll verdeutlichen, welche Vorteile wir (Bild-Kontor.de) dank Zeitwabe und LobPunkt haben:
Der Betrachter soll diese Zahlen auf einen Blick werten und die Vorteile für SEIN GESCHÄFT erkennen können. Zum Beispiel anhand einer Zeitleiste, die die Entwicklung der verschiedenen Kennzahlen wiedergibt.
Die Kennzahlen (die Entwicklung) können Sie hier aufrufen: https://ablage-beispiel.de/ordner/7KrtWmPq2ZxN8-vbYy3HsLd0QaTeRcU?teilen=ja
Besonders soll die positive Entwicklung ab Ende September 2017 deutlich werden. Ab Ende September 2017 haben wir Zeitwabe und LobPunkt.com für die Terminvereinbarung genutzt. Vorher haben wir Termine per Email und Telefon vereinbart, was deutlich zeitintensiver war.
Das Design der Zeitleiste (der Infografik) soll sich an Zeitwabe.de orientieren.
Falls die sechs Kennzahlen nicht übersichtlich in einer Zeitleiste darstellbar sind, könnten die Kennzahlen auf mehrere Grafiken aufgeteilt werden.
Vorstellbar ist auch eine interaktive Infografik, bei der man die jeweilige Kennzahl auswählen kann.
Wir lassen uns hier gerne von Ihrer Kreativität überraschen. Der spätere Kunde/Nutzer/ Betrachter der Infografik steht bitte im Vordergrund jeder Überlegung/jedes Designs.
Nutzen Sie ggf. bitte Icons und verschiedenen Farben, um die verschiedenen Kennzahlen auch visuell zu verdeutlichen.
Die Infografik soll später auf https://entwickler.zeitwabe.de/de/ueber-uns.html und in Flyern veröffentlicht werden.
Wesentliche Funktionen und Vorteile siehe auch:
https://www.videoportal-beispiel.de/watch?v=qRtmZZk_31p
https://www.videoportal-beispiel.de/watch?v=wLpoNNe_74x
Die einzelnen gr..

```html
<!DOCTYPE html>
<html lang="de">
<head>
<meta charset="utf-8">
<title>Zeitwabe – Kennzahlen im Zeitverlauf</title>
<link rel="stylesheet" href="https://fonts.googleapis.com/css2?family=Exo+2:wght@600;700;800&family=Open+Sans:wght@400;600&display=swap">
<style>
  :root {
    --red: #e30613;
    --green: #8ab823;
    --yellow: #fdc900;
    --chart-light: #cdd5da;
    --chart-dark: #aebac2;
    --chart-fade: #f6f7f8;
    --axis: #8795a0;
    --caption: #6c7880;
    --white: #ffffff;
  }
  * { margin: 0; padding: 0; box-sizing: border-box; }
  html, body { width: 1200px; height: 726px; overflow: hidden; background: var(--white); }
  .canvas { position: relative; width: 1200px; height: 726px; }
  .panel { position: absolute; width: 370px; height: 245px; overflow: visible; }
  .label { font-family: "Exo 2", sans-serif; font-weight: 700; font-size: 12px; letter-spacing: 1.2px; fill: var(--white); }
  .caption { font-family: "Exo 2", sans-serif; font-weight: 600; font-size: 11px; letter-spacing: 0.4px; fill: var(--caption); }
  .axis-text { font-family: "Open Sans", sans-serif; font-size: 8px; fill: var(--white); }
  .delta { font-family: "Exo 2", sans-serif; font-weight: 800; font-size: 23px; letter-spacing: 1.5px; }
  .delta .sign, .delta .pct { font-weight: 600; }
  .trend { fill: none; stroke-width: 5; stroke-linejoin: round; stroke-linecap: round; }
</style>
</head>
<body>
<main class="canvas">
  <svg width="0" height="0" style="position:absolute">
    <defs>
      <linearGradient id="usage-shade" x1="0" x2="1" y1="0" y2="0">
        <stop offset="0" stop-color="var(--chart-dark)"/>
        <stop offset="1" stop-color="var(--chart-fade)"/>
      </linearGradient>
    </defs>
  </svg>

  <!-- Shootings -->
  <svg class="panel" style="left:18px;top:89px" viewBox="0 0 370 245">
    <g transform="translate(1,20)">
      <rect x="0" y="17" width="344.5" height="201" fill="var(--chart-light)"/>
      <rect x="92" y="17" width="252.5" height="201" fill="url(#usage-shade)"/>
      <rect x="0" y="204.5" width="344.5" height="13.5" fill="var(--axis)"/>
      <text class="axis-text" x="9" y="214.5">MAI 17</text>
      <text class="axis-text" x="75" y="214.5">OKT 17</text>
      <text class="axis-text" x="340" y="214.5" text-anchor="end">SEP 18</text>
      <text class="caption" x="98" y="195">Nutzung Zeitwabe und LobPunkt</text>
      <polyline class="trend" stroke="var(--red)" points="11,182 31,192 51,172 71,182 91,172 110,152 128,143 147,182 167,114 186,85 206,45 225,65 244,95 264,75 283,124 302,154 321,25"/>
      <text class="delta" x="228" y="39" fill="var(--red)"><tspan class="sign">+ </tspan>XX <tspan class="pct">%</tspan></text>
      <rect x="-0.5" y="0" width="147" height="17" fill="var(--red)"/>
      <rect x="-0.5" y="0" width="47.5" height="47.5" fill="var(--red)"/>
      <g role="img" aria-label="Kamera-Symbol"><circle cx="23.5" cy="24" r="21" fill="var(--white)"/><circle cx="23.5" cy="25" r="13" fill="var(--green)"/><circle cx="23.5" cy="25" r="6" fill="var(--yellow)"/></g>
      <text class="label" x="103" y="13" text-anchor="middle">SHOOTINGS</text>
      <g transform="translate(335,-1.5)"><circle r="14.5" fill="var(--red)"/><circle cx="-2" cy="-2" r="5.5" fill="none" stroke="var(--white)" stroke-width="2.5"/><line x1="2" y1="2" x2="7" y2="7" stroke="var(--white)" stroke-width="3" stroke-linecap="round"/></g>
    </g>
  </svg>

  <!-- Kunden -->
  <svg class="panel" style="left:384.5px;top:89px" viewBox="0 0 370 245">
    <g transform="translate(1,20)">
      <rect x="0" y="17" width="344.5" height="201" fill="var(--chart-light)"/>
      <rect x="91" y="17" width="253.5" height="201" fill="url(#usage-shade)"/>
      <rect x="0" y="204.5" width="344.5" height="13.5" fill="var(--axis)"/>
      <text class="axis-text" x="8" y="214.5">MAI 17</text>
      <text class="axis-text" x="75" y="214.5">OKT 17</text>
      <text class="axis-text" x="339" y="214.5" text-anchor="end">SEP 18</text>
      <text class="caption" x="97" y="195">Nutzung Zeitwabe und LobPunkt</text>
      <polyline class="trend" stroke="var(--green)" points="7.5,175 28.5,183 47.5,166 67.5,175 87.5,166 107.5,138 127.5,135 147.5,171 166.5,111 186.5,86 206.5,51 226.5,68 246.5,94 265.5,77 285.5,120 305.5,145 324.5,34"/>
      <text class="delta" x="233" y="51" fill="var(--green)"><tspan class="sign">+ </tspan>XX <tspan class="pct">%</tspan></text>
      <rect x="0" y="0" width="146" height="17" fill="var(--green)"/>
      <rect x="0" y="0" width="47.5" height="47.5" fill="var(--green)"/>
      <g role="img" aria-label="Kunden-Symbol"><circle cx="23.5" cy="24" r="21" fill="var(--white)"/><circle cx="23.5" cy="25" r="12" fill="var(--yellow)"/><circle cx="26" cy="28" r="7" fill="var(--red)"/></g>
      <text class="label" x="111" y="13" text-anchor="middle">KUNDEN</text>
      <g transform="translate(335,-1.5)"><circle r="14.5" fill="var(--green)"/><circle cx="-2" cy="-2" r="5.5" fill="none" stroke="var(--white)" stroke-width="2.5"/><line x1="2" y1="2" x2="7" y2="7" stroke="var(--white)" stroke-width="3" stroke-linecap="round"/></g>
    </g>
  </svg>

  <!-- Umsatz -->
  <svg class="panel" style="left:753px;top:89px" viewBox="0 0 370 245">
    <g transform="translate(1,20)">
      <rect x="0" y="17" width="344" height="201" fill="var(--chart-light)"/>
      <rect x="91" y="17" width="253" height="201" fill="url(#usage-shade)"/>
      <rect x="0" y="204.5" width="344" height="13.5" fill="var(--axis)"/>
      <text class="axis-text" x="8" y="214.5">MAI 17</text>
      <text class="axis-text" x="75" y="214.5">OKT 17</text>
      <text class="axis-text" x="339" y="214.5" text-anchor="end">SEP 18</text>
      <text class="caption" x="96" y="195">Nutzung Zeitwabe und LobPunkt</text>
      <polyline class="trend" stroke="var(--yellow)" points="6,157 27,161 47,161 67,165 87,161 107,154 127,150 147,154 167,146 187,137 207,114 227,119 247,98 267,106 287,78 307,82 328,55"/>
      <text class="delta" x="255" y="50" fill="var(--yellow)"><tspan class="sign">+ </tspan>74 <tspan class="pct">%</tspan></text>
      <rect x="0" y="0" width="147" height="17" fill="var(--yellow)"/>
      <rect x="0" y="0" width="47.5" height="47.5" fill="var(--yellow)"/>
      <g role="img" aria-label="Münzstapel-Symbol"><circle cx="23.5" cy="24" r="21" fill="var(--white)"/><rect x="14" y="13" width="10" height="22" rx="4" fill="var(--green)"/><rect x="25" y="23" width="10" height="12" rx="4" fill="var(--red)"/></g>
      <text class="label" x="113" y="13" text-anchor="middle">UMSATZ</text>
      <g transform="translate(339,-1.5)"><circle r="14.5" fill="var(--yellow)"/><circle cx="-2" cy="-2" r="5.5" fill="none" stroke="var(--white)" stroke-width="2.5"/><line x1="2" y1="2" x2="7" y2="7" stroke="var(--white)" stroke-width="3" stroke-linecap="round"/></g>
    </g>
  </svg>

  <!-- Werbekosten -->
  <svg class="panel" style="left:17.5px;top:330px" viewBox="0 0 370 245">
    <g transform="translate(1,20)">
      <rect x="0" y="17" width="344.5" height="200.5" fill="var(--chart-light)"/>
      <rect x="91.5" y="17" width="253" height="200.5" fill="url(#usage-shade)"/>
      <rect x="0" y="204" width="344.5" height="13.5" fill="var(--axis)"/>
      <text class="axis-text" x="8" y="214">MAI 17</text>
      <text class="axis-text" x="73" y="214">OKT 17</text>
      <text class="axis-text" x="340" y="214" text-anchor="end">SEP 18</text>
      <text class="caption" x="98" y="36">Nutzung Zeitwabe und LobPunkt</text>
      <polyline class="trend" stroke="var(--yellow)" points="11.5,63 31.5,77 51.5,54 71.5,63 91.5,63 110.5,129 130.5,161 149.5,171 168.5,171 188.5,184 208.5,184 228.5,171 248.5,161 267.5,171 287.5,194 307.5,184 327.5,171"/>
      <text class="delta" x="253" y="149" fill="var(--yellow)"><tspan class="sign">- </tspan>33 <tspan class="pct">%</tspan></text>
      <rect x="0" y="0" width="147" height="17" fill="var(--yellow)"/>
      <rect x="0" y="0" width="47.5" height="47.5" fill="var(--yellow)"/>
      <g role="img" aria-label="Megafon-Symbol"><circle cx="23.5" cy="24" r="21" fill="var(--white)"/><polygon points="12,20 28,12 28,36 12,28" fill="var(--green)"/><circle cx="33" cy="24" r="3" fill="var(--red)"/></g>
      <text class="label" x="97" y="13" text-anchor="middle">WERBEKOSTEN</text>
      <g transform="translate(330,-1.5)"><circle r="14.5" fill="var(--yellow)"/><circle cx="-2" cy="-2" r="5.5" fill="none" stroke="var(--white)" stroke-width="2.5"/><line x1="2" y1="2" x2="7" y2="7" stroke="var(--white)" stroke-width="3" stroke-linecap="round"/></g>
    </g>
  </svg>

  <!-- No-Show-Rate -->
  <svg class="panel" style="left:385.5px;top:330px" viewBox="0 0 370 245">
    <g transform="translate(1,20)">
      <rect x="0" y="17" width="344.5" height="200.5" fill="var(--chart-light)"/>
      <rect x="90.5" y="17" width="254" height="200.5" fill="url(#usage-shade)"/>
      <rect x="0" y="204" width="344.5" height="13.5" fill="var(--axis)"/>
      <text class="axis-text" x="8" y="214">MAI 17</text>
      <text class="axis-text" x="92" y="214">OKT 17</text>
      <text class="axis-text" x="339" y="214" text-anchor="end">SEP 18</text>
      <text class="caption" x="95" y="39">Nutzung Zeitwabe und LobPunkt</text>
      <polyline class="trend" stroke="var(--red)" points="8.5,61 29.5,77 49.5,54 68.5,84 88.5,69 107.5,169 127.5,176 147.5,184 167.5,168 187.5,183 207.5,190 226.5,183 246.5,190 266.5,198 286.5,190 306.5,183 326.5,190"/>
      <text class="delta" x="251" y="171" fill="var(--red)"><tspan class="sign">- </tspan>XX <tspan class="pct">%</tspan></text>
      <rect x="0" y="0" width="147" height="17" fill="var(--red)"/>
      <rect x="0" y="0" width="47.5" height="47.5" fill="var(--red)"/>
      <g role="img" aria-label="Wartesessel-Symbol"><circle cx="23.5" cy="24" r="21" fill="var(--white)"/><rect x="12" y="14" width="23" height="20" rx="3" fill="var(--green)"/><rect x="17" y="10" width="13" height="12" rx="2" fill="var(--yellow)"/></g>
      <text class="label" x="95" y="13" text-anchor="middle">NO-SHOW-RATE</text>
      <g transform="translate(332,-1.5)"><circle r="14.5" fill="var(--red)"/><circle cx="-2" cy="-2" r="5.5" fill="none" stroke="var(--white)" stroke-width="2.5"/><line x1="2" y1="2" x2="7" y2="7" stroke="var(--white)" stroke-width="3" stroke-linecap="round"/></g>
    </g>
  </svg>

  <!-- Zeitaufwand -->
  <svg class="panel" style="left:753px;top:330px" viewBox="0 0 370 245">
    <g transform="translate(1,20)">
      <rect x="0" y="17" width="344" height="201" fill="var(--chart-light)"/>
      <rect x="89" y="17" width="255" height="201" fill="url(#usage-shade)"/>
      <rect x="0" y="204.5" width="344" height="13.5" fill="var(--axis)"/>
      <text class="axis-text" x="8" y="214.5">MAI 17</text>
      <text class="axis-text" x="73" y="214.5">OKT 17</text>
      <text class="axis-text" x="339" y="214.5" text-anchor="end">SEP 18</text>
      <text class="caption" x="95" y="39">Nutzung Zeitwabe und LobPunkt</text>
      <polyline class="trend" stroke="var(--green)" points="8,62 29,65 49,57 70,63 91,57 111,190 132,196 152,193 172,190 193,193 213,190 233,193 253,190 273,196 294,199 314,196 334,188"/>
      <text class="delta" x="264" y="175" fill="var(--green)"><tspan class="sign">- </tspan>XX <tspan class="pct">%</tspan></text>
      <rect x="0" y="0" width="147" height="17" fill="var(--green)"/>
      <rect x="0" y="0" width="47.5" height="47.5" fill="var(--green)"/>
      <g role="img" aria-label="Stoppuhr-Symbol"><circle cx="23.5" cy="24" r="21" fill="var(--white)"/><circle cx="23.5" cy="26" r="14" fill="var(--green)"/><circle cx="23.5" cy="26" r="10" fill="var(--yellow)"/></g>
      <text class="label" x="94" y="13" text-anchor="middle">ZEITAUFWAND</text>
      <g transform="translate(339,-1.5)"><circle r="14.5" fill="var(--green)"/><circle cx="-2" cy="-2" r="5.5" fill="none" stroke="var(--white)" stroke-width="2.5"/><line x1="2" y1="2" x2="7" y2="7" stroke="var(--white)" stroke-width="3" stroke-linecap="round"/></g>
    </g>
  </svg>
</main>
</body>
</html>
```